Create a landing page for a new product market combination for an international software company

We are a software company being in the BtoB market for over 20 years. Our product is a software tool that allows for very flexible and versatile cost calculations for companies. We sell to all industries in over 40 countries with 500 clients. We have fairly recently seen a succesfull "competitor" (www.quorvel.com) come up in the niche market of IT costing. This competitor has launched an independent platform with regards to managing IT costs (www.PLXguild.org). In this independent platform standards are set, events are organised and books are written. Since our software can handle all type of costing questions we can en already do play a role in IT costing. We have therefore become a sponsor of the PLX guild. Besides that we came accross the opportunity to buy the URL: www.plxsoftware.com Which we did. We are now looking for a design on that landing page that communicates the fact that the visitor has landed with a company that have in depth knowledge on the PLX subject and provide an effective an affordable tooling for PLX. Currently the difference between the professionalism of our own website (www.brandivex.com) and that of the competitor (www.quorvel.com) and the independent council (www.plxguild.org). is too big.

Target Market(s)

BtB with large IT spend

Number of Pages Required

1 page

Colors

Designer to choose colors to be used in the design.

Requirements
Must have
• A proffessional look and feel
Should not have
• Definetely not too much information and wording

```html
<!DOCTYPE html>
<html lang="en">
<head>
<meta charset="utf-8">
<title>PLX Software – Manage Costs and Performance</title>
<link rel="stylesheet" href="https://fonts.googleapis.com/css2?family=Arimo:wght@400;700&family=Gelasio:wght@400&display=swap">
<style>
:root{
  --nav:#6870be;
  --nav-text:#ffffff;
  --cta-border:#c2405c;
  --overlay:rgba(58,63,82,0.86);
  --hero-top:#2f5d66;
  --hero-mid:#3d4a5a;
  --hero-bottom:#5e7a4a;
  --light-bg:#e9ebf2;
  --ink:#1b1b1b;
  --grey:#6d6d6d;
  --white:#ffffff;
  --globe:#3f7fd0;
}
*{margin:0;padding:0;box-sizing:border-box}
html,body{width:876px;height:1200px;overflow:hidden}
body{position:relative;font-family:"Arimo",Arial,sans-serif;background:var(--white);color:var(--ink)}
.abs{position:absolute}
.serif{font-family:"Gelasio",Georgia,serif;font-weight:400}

/* navigation */
.nav{left:0;top:0;width:876px;height:70px;background:var(--nav)}
.nav-item{top:32px;font-size:6.6px;font-weight:700;color:var(--nav-text);letter-spacing:.1px}
.cta{left:773px;top:22px;width:81px;height:28px;border:1px solid var(--cta-border);border-radius:6px;color:var(--nav-text);font-size:6.6px;font-weight:700;display:flex;align-items:center;justify-content:center}

/* hero */
.hero-photo{left:0;top:70px;width:876px;height:431px;background:linear-gradient(170deg,var(--hero-top) 0%,#6d8a96 12%,var(--hero-mid) 30%,#4a5060 70%,var(--hero-bottom) 90%,#c27a4a 100%)}
.hero-panel{left:0;top:120px;width:876px;height:330px;background:var(--overlay)}
.hero-title{left:164px;top:134px;font-size:19px;line-height:22.5px;color:var(--white)}
.body-copy{font-size:6.2px;line-height:10.9px;color:var(--white)}
.ph{border-radius:0}
.ph-laptop{left:164px;top:280px;width:164px;height:123px;background:linear-gradient(135deg,#b9a27e,#e8e6e2 45%,#2a2a2a 80%)}
.ph-finance{left:547px;top:184px;width:164px;height:219px;background:linear-gradient(180deg,#6b4a36,#e9e7e2 30%,#dcdad4 75%,#6b4a36)}

/* technology section */
.tech{left:0;top:501px;width:876px;height:467px;background:linear-gradient(180deg,#f4f5f9 0%,var(--light-bg) 50%,#d9dde8 100%)}
.tech-title{left:145px;top:594px;font-size:18px;line-height:22.5px;color:var(--ink)}
.tech-copy{left:145px;top:654px;width:296px;font-size:6.2px;line-height:10.9px;color:var(--ink)}
.caption{left:145px;top:734px;font-size:6px;font-weight:700;color:var(--ink)}
.webpage{left:398px;top:733px;display:flex;align-items:center;gap:4px;font-size:6.4px;font-weight:700;color:var(--ink)}
.ph-handshake{left:145px;top:764px;width:295px;height:132px;background:linear-gradient(135deg,#f2f2f2,#9a9a9a 50%,#2c2c2c)}
.ph-team{left:470px;top:596px;width:296px;height:168px;background:linear-gradient(180deg,#1b2a8a,#3a6fd0 55%,#cfd9ef)}
.card{left:470px;top:764px;width:296px;height:132px;background:var(--grey);padding:28px 0 0 52px;color:var(--white)}
.card-title{font-size:9.8px;font-weight:700;margin-bottom:9px}
.card-copy{font-size:6.2px;line-height:10.9px;width:170px}

/* closing */
.closing{left:0;top:968px;width:876px;height:232px;background:var(--grey);text-align:center;color:var(--white)}
.closing-title{margin-top:85px;font-size:17.6px}
.closing-copy{margin:11px auto 0;width:250px;font-size:6.2px;line-height:10.9px}
</style>
</head>
<body>
<header class="abs nav">
  <span class="abs nav-item" style="left:385px">HOME</span>
  <span class="abs nav-item" style="left:422px">PRODUCT</span>
  <span class="abs nav-item" style="left:473px">MARKETS</span>
  <span class="abs nav-item" style="left:524px">COMPANY</span>
  <span class="abs nav-item" style="left:575px">PARTNERS</span>
  <span class="abs nav-item" style="left:629px">EVENTS</span>
  <span class="abs nav-item" style="left:673px">SUPPORT</span>
  <span class="abs nav-item" style="left:723px">CONTACT</span>
  <span class="abs cta">GET STARTED</span>
</header>

<section>
  <div class="abs hero-photo" role="img" aria-label="Upward view of glass office towers against a cloudy sky"></div>
  <div class="abs hero-panel"></div>
  <h1 class="abs serif hero-title">Software to Manage<br>Costs and<br>Performance</h1>
  <p class="abs body-copy" style="left:164px;top:208px;width:166px">Lorem ipsum dolor sit amet, consectetur adipisifwcing elit, sed do eiusmod tempor incididunt ut labore et dolore roipi magna aliqua. Ut enim ad minim veeniam, quis nostruklad exercitation ullamco laboris nisi ut aliquip ex ea commodo consequat. Duis aute irure dolor in reprehenderit in tufpoy voluptate velit esse cillum dolore eu fugiat nulla parieratur.</p>
  <div class="abs ph ph-laptop" role="img" aria-label="Laptop and tablet showing bar and pie charts on a desk"></div>
  <div class="abs body-copy" style="left:356px;top:208px;width:166px">
    <p>Culpa qui officia deserunt mollit anim id est laborum. Sed ut perspiciatis unde omnis iste natus error sit voluptartem accusantium doloremque laudantium, totam rem aperiam, eaque ipsa quae ab illo inventore veritatis et quasi ropeior architecto beatae vitae dicta sunt explicabo. Nemo eniem ipsam voluptatem quia voluptas sit aspernatur aut odit aut fugit, sed quia consequuntur magni dolores eosep quiklop ratione voluptatem sequi nesciunt. Neque porro quisquam est, quepi dolorem ipsum quia dolor srit amet, consectetur adipisci velit, seld quia non numquam eiuris modi tempora incidunt ut labore et dolore magnam aliquam quaerat iope voluptatem.</p>
    <p style="margin-top:10px">Lorem ipsum dolor sit amet, consectetur adipisifwcing elit, sed do eiusmod tempor incididunt ut labore et dolore roipi magna aliqua. Ut enim ad minim veeniam, quis nostruklad exercitation ullamco laboris nisi ut aliquip ex ea commodo consequat. Duis aute irure dolor in reprehenderit in tufpoy</p>
  </div>
  <div class="abs ph ph-finance" role="img" aria-label="Hands over a desk with a sketched finance plan, coffee cup and laptop"></div>
</section>

<section>
  <div class="abs tech" role="img" aria-label="Faded view of city skyscrapers"></div>
  <h2 class="abs serif tech-title">Technology and the Business<br>understand each other through PLX</h2>
  <p class="abs tech-copy">Lorem ipsum dolor sit amet, consectetur adipisicing elit, sed do eiusmod tempor incididunt ut ero labore et dolore magna aliqua. Ut enim ad minim veniam, quis nostrud exercitation ullamco poriti laboris nisi ut aliquip ex ea commodo consequat. Duis aute irure dolor in reprehenderit in uienply voluptate velit esse cillum dolore eu fugiat nulla pariatur. Excepteur sint occaecat cupidatat norin proident, sunt in culpa qui officia deserunt mollit anim id est laborum.</p>
  <span class="abs caption">LOREM IPSUM DOLOR AMET CONSECTETUER</span>
  <span class="abs webpage">
    <svg width="8" height="8" viewBox="0 0 10 10" aria-hidden="true"><circle cx="5" cy="5" r="4.5" fill="var(--globe)"/><path d="M1 5h8M5 .5c2 2.5 2 6.5 0 9M5 .5c-2 2.5-2 6.5 0 9" stroke="#fff" stroke-width=".7" fill="none"/></svg>
    webpage
  </span>
  <div class="abs ph ph-handshake" role="img" aria-label="Black and white business handshake"></div>
  <div class="abs ph ph-team" role="img" aria-label="Silhouettes of a business team in front of blue financial charts"></div>
  <div class="abs card">
    <h3 class="card-title">Manage Technology as a Business: PLX</h3>
    <p class="card-copy">Lorem ipsum dolor sit amet, consectetur adipisicing elit, sed do eiusmod tempor incididunt ut ero labore et dolore magna aliqua. Ut enim ad minim veniam.</p>
  </div>
</section>

<section class="abs closing">
  <h2 class="serif closing-title">Excepteur occaeuiecat cupidatat.</h2>
  <p class="closing-copy">Lorem ipsum dolor sit amet, consectetur adipisicing elit, sed do eiusmod tempor incididunt ut ero labore et dolore magna aliqua. Ut enim ad minim veniam, quis nostrud exercitation ullamco.</p>
</section>
</body>
</html>
```